CD cover

It's about a music CD.
Artist: PEBBLES AND COMPANY
Title: VELVET CURVES
Style: jazz-pop
Ideas: dancing flowers, something playful, something beautiful
possible elements: flowers, music, oriental shapes, something colorful

Target Market(s)

Music consumers from Tunezzo and Co.

Industry/Entity Type

Musik

Requirements
Nice to have
• Attached are two examples (dancing flowers)

```html
<!DOCTYPE html>
<html lang="en">
<head>
<meta charset="utf-8">
<title>Pebbles and Company – Velvet Curves</title>
<link rel="stylesheet" href="https://fonts.googleapis.com/css2?family=Titan+One&display=swap">
<style>
  :root {
    --page-bg: #e9eaec;
    --cream: #f4ebe2;
    --ink: #141414;
    --petal-blue: #3fc6ea;
    --petal-orange: #f68a1e;
    --petal-yellow: #f7c61f;
    --sunrise: #fbe7a8;
    --rose: #f6a3b8;
  }
  * { margin: 0; padding: 0; box-sizing: border-box; }
  html, body {
    width: 1200px;
    height: 846px;
    overflow: hidden;
    background: var(--page-bg);
  }
  .cover {
    position: absolute;
    left: 187px;
    top: 43px;
    width: 825px;
    height: 760px;
    overflow: hidden;
  }
  .cover-artwork {
    position: absolute;
    inset: 0;
    background: linear-gradient(160deg,
      var(--rose) 0%,
      var(--sunrise) 22%,
      var(--petal-yellow) 40%,
      var(--petal-orange) 58%,
      var(--petal-blue) 78%,
      #2a8fc8 100%);
  }
  .cover-type {
    position: absolute;
    inset: 0;
    width: 100%;
    height: 100%;
  }
  .artist-name {
    font-family: "Titan One", sans-serif;
    font-size: 124px;
    text-anchor: middle;
  }
  .artist-name.layer-shadow { fill: var(--ink); stroke: var(--ink); stroke-width: 6px; stroke-linejoin: round; }
  .artist-name.layer-face { fill: var(--cream); }
  .album-name {
    font-family: "Titan One", sans-serif;
    font-size: 52px;
    letter-spacing: 2px;
    text-anchor: middle;
  }
  .album-name.layer-shadow { fill: var(--ink); stroke: var(--ink); stroke-width: 6px; stroke-linejoin: round; }
  .album-name.layer-face { fill: var(--cream); }
</style>
</head>
<body>
  <main class="cover">
    <div class="cover-artwork" role="img" aria-label="Retro psychedelic illustration of large blue, orange and yellow flowers beneath pastel rainbow swirls and a sunny sky"></div>

    <svg class="cover-type" viewBox="0 0 825 760" aria-label="Pebbles and Company – Velvet Curves">
      <defs>
        <g id="artist-lines">
          <text x="412" y="190" textLength="540" lengthAdjust="spacingAndGlyphs">Pebbles</text>
          <text x="412" y="335" textLength="260" lengthAdjust="spacingAndGlyphs">and</text>
          <text x="412" y="480" textLength="560" lengthAdjust="spacingAndGlyphs">Company</text>
        </g>
      </defs>

      <g class="artist-name layer-shadow" transform="translate(6 7)"><use href="#artist-lines"/></g>
      <g class="artist-name layer-face"><use href="#artist-lines"/></g>

      <text class="album-name layer-shadow" x="415" y="698" textLength="520" lengthAdjust="spacingAndGlyphs">VELVET CURVES</text>
      <text class="album-name layer-face" x="411" y="693" textLength="520" lengthAdjust="spacingAndGlyphs">VELVET CURVES</text>
    </svg>
  </main>
</body>
</html>
```